Business Card Design Project - IT Company

Kestrafield Information Technology Solutions
We are an Information Technology Company. We provide computer services to commercial companies. We would like a new card full color front and back with bleeding edge.
We have a logo that you can use or if you want to come up with a new logo that is fine too.
Our colors are mostly Maroon and black but be creative.
Sample Information
Brent R Okafor
4812 W Saguaro Ridge Drive
Suite 600
Phoenix, AZ 85016
O: 602.914.2037
C: 602.468.1290
24/7: 888.914.2037
bokafor@kestrafield.example
www.kestrafield.example
Target Market(s)
Business of all sizes
Industry/Entity Type
Computer
Requirements
Must have
- Bleeding edge
full color on both sides

```html
<!DOCTYPE html>
<html lang="en">
<head>
<meta charset="utf-8">
<title>Kestrafield Business Card Concepts</title>
<link rel="stylesheet" href="https://fonts.googleapis.com/css2?family=Arimo:wght@400;700&display=swap">
<style>
  :root {
    --page: #ffffff;
    --page-edge: #c9c9c9;
    --maroon: #4a1a1c;
    --maroon-soft: #5e2a2c;
    --band: #221617;
    --ink: #ffffff;
    --accent: #ece21a;
    --logo-square: #6a2326;
  }
  * { box-sizing: border-box; margin: 0; padding: 0; }
  html, body { width: 1200px; height: 1059px; overflow: hidden; background: var(--page); }
  body { font-family: "Arimo", Arial, sans-serif; color: var(--ink); }

  .sheet {
    position: relative;
    width: 1200px; height: 1059px;
    border: 1px solid var(--page-edge);
  }
  .card {
    position: absolute;
    width: 494px; height: 281px;
    background: var(--maroon);
    overflow: hidden;
  }
  .col-front { left: 83px; }
  .col-back { left: 625px; }
  .row-1 { top: 71px; }
  .row-2 { top: 389px; }
  .row-3 { top: 707px; }

  /* Soft tonal areas where artwork sits */
  .art { position: absolute; }
  .art-globe {
    left: -40px; top: -10px; width: 170px; height: 230px;
    background: radial-gradient(ellipse at 45% 35%, var(--maroon-soft) 0%, rgba(94,42,44,0.5) 55%, rgba(74,26,28,0) 75%);
  }
  .row-3 .art-globe { top: -60px; height: 210px; width: 150px; }
  .art-device-low {
    right: -20px; bottom: -20px; width: 120px; height: 90px;
    background: radial-gradient(ellipse at 55% 55%, var(--maroon-soft) 0%, rgba(74,26,28,0) 70%);
  }
  .art-device-high {
    right: -10px; top: -15px; width: 170px; height: 110px;
    background: radial-gradient(ellipse at 50% 50%, var(--maroon-soft) 0%, rgba(74,26,28,0) 70%);
  }

  .dark-sweep { position: absolute; inset: 0; width: 494px; height: 281px; }
  .dark-sweep path { fill: var(--band); }

  /* Front: company name lockup */
  .brand {
    position: absolute;
    display: flex; align-items: center; gap: 10px;
  }
  .brand-mark {
    width: 46px; height: 52px;
    background: var(--logo-square);
  }
  .brand-name {
    display: flex; flex-direction: column;
    font-weight: 700; color: var(--ink);
  }
  .brand-word { font-size: 44px; line-height: 1; letter-spacing: 0.5px; }
  .brand-tag { font-size: 11.5px; line-height: 1.4; margin-top: 3px; }
  .row-1 .brand, .row-2 .brand { left: 154px; top: 108px; }
  .row-3 .brand { left: 134px; top: 86px; }

  /* Back: contact details */
  .holder { font-weight: 700; font-size: 18px; letter-spacing: 0.2px; }
  .details { font-size: 15px; line-height: 20px; letter-spacing: 0.3px; }
  .web-band {
    position: absolute; left: 0; right: 0; bottom: 0;
    height: 33px;
    background: var(--band);
    display: flex; align-items: center; justify-content: center;
    font-size: 17px; letter-spacing: 3px;
  }
  .web-band .domain { color: var(--accent); }

  .back-stacked .holder { position: absolute; left: 26px; top: 48px; }
  .back-stacked .details { position: absolute; left: 26px; top: 112px; }

  .back-columns .holder { position: absolute; left: 0; right: 0; top: 108px; text-align: center; }
  .back-columns .details { position: absolute; top: 158px; font-size: 14px; }
  .back-columns .details-left { right: 272px; text-align: right; }
  .back-columns .details-right { left: 238px; }
  .back-columns .web-band { height: 34px; }

  .back-banded .holder { position: absolute; left: 0; right: 0; top: 153px; text-align: center; }
  .back-banded .info-band {
    position: absolute; left: 0; right: 0; bottom: 0;
    height: 93px;
    background: var(--band);
    display: flex; flex-direction: column; align-items: center; justify-content: center;
    font-size: 15px; line-height: 21px; letter-spacing: 0.2px; text-align: center;
  }
</style>
</head>
<body>
<main class="sheet">

  <!-- Concept 1 -->
  <section class="card col-front row-1" aria-label="Front, concept 1">
    <div class="art art-globe" role="img" aria-label="Wireframe globe artwork"></div>
    <div class="art art-device-low" role="img" aria-label="Computer mouse outline artwork"></div>
    <div class="brand">
      <span class="brand-mark"></span>
      <span class="brand-name"><span class="brand-word">Kestrafield</span><span class="brand-tag">Information Technology Solutions</span></span>
    </div>
  </section>

  <section class="card col-back row-1 back-stacked" aria-label="Back, concept 1">
    <div class="art art-device-high" role="img" aria-label="Computer mouse outline artwork"></div>
    <p class="holder">Brent R Okafor</p>
    <p class="details">4812 W Saguaro Ridge Drive<br>Suite 600, Phoenix, AZ 85016<br>O: 602.914.2037<br>C: 602.468.1290<br>24/7: 888.914.2037<br>bokafor@kestrafield.example</p>
    <p class="web-band">www.<span class="domain">kestrafield</span>.example</p>
  </section>

  <!-- Concept 2 -->
  <section class="card col-front row-2" aria-label="Front, concept 2">
    <div class="art art-globe" role="img" aria-label="Wireframe globe artwork"></div>
    <div class="art art-device-low" role="img" aria-label="Computer mouse outline artwork"></div>
    <div class="brand">
      <span class="brand-mark"></span>
      <span class="brand-name"><span class="brand-word">Kestrafield</span><span class="brand-tag">Information Technology Solutions</span></span>
    </div>
  </section>

  <section class="card col-back row-2 back-columns" aria-label="Back, concept 2">
    <div class="art art-device-high" role="img" aria-label="Computer mouse outline artwork"></div>
    <p class="holder">Brent R Okafor</p>
    <p class="details details-left">C: 602.468.1290<br>bokafor@kestrafield.example</p>
    <p class="details details-right">4812 W Saguaro Ridge Drive<br>Suite 600, Phoenix, AZ 85016<br>O: 602.914.2037<br>24/7: 888.914.2037</p>
    <p class="web-band">www.<span class="domain">kestrafield</span>.example</p>
  </section>

  <!-- Concept 3 -->
  <section class="card col-front row-3" aria-label="Front, concept 3">
    <svg class="dark-sweep" viewBox="0 0 494 281" aria-hidden="true">
      <path d="M0 170 C60 200 140 225 220 230 C300 236 360 250 400 281 L0 281 Z"/>
    </svg>
    <div class="art art-globe" role="img" aria-label="Wireframe globe artwork"></div>
    <div class="art art-device-low" role="img" aria-label="Computer mouse outline artwork"></div>
    <div class="brand">
      <span class="brand-mark"></span>
      <span class="brand-name"><span class="brand-word">Kestrafield</span><span class="brand-tag">Information Technology Solutions</span></span>
    </div>
  </section>

  <section class="card col-back row-3 back-banded" aria-label="Back, concept 3">
    <div class="art art-device-high" role="img" aria-label="Computer mouse outline artwork"></div>
    <p class="holder">Brent R Okafor</p>
    <div class="info-band">
      <p>4812 W Saguaro Ridge Drive, Suite 600, Phoenix, AZ 85016</p>
      <p>O: 602.914.2037, C: 602.468.1290, 24/7: 888.914.2037</p>
      <p>bokafor@kestrafield.example, www.kestrafield.example</p>
    </div>
  </section>

</main>
</body>
</html>
```